Accommodation in an Executive Apartment for rent could be a Bed and breakfast,

Currently have a website and like the overall look but it needs revamping and want to add an instant booking button, which I would do later as the unit has a channel manager. Also want to be able to post blogs, etc. Need it to be viewed well on smart phones/tablets. all information related to this unit is on the current site which is www.lorvenstaysmirrabrook.com.au if you would view websites similar to staywell.example and roamtrip.example Must be able to be coded in Wordpress

The current design is done in Wordpress so would want this functionality in any new design.

Target Market(s)

Workers at Quorran precinct, Canberra. Workers at Halvern centre Deakin, Workers at Marlow Peter Tenby Hospital, Workers at Brindlewood Hospital, Public Servants Woden, Workers in Deakin ACT

Industry/Entity Type

Accommodation

Number of Pages Required

5+ page

Font styles to use
Sans Serif

Colors
ec1f27

Requirements
Must have
• Must have a classy look about it. Less clicks through the better. Not to wordy. Hard hitting points,
Nice to have
• Would like to retain the same colour theme and look
Should not have
• anything tacky

```html
<!DOCTYPE html>
<html lang="en">
<head>
<meta charset="utf-8">
<title>Lorven Stays – Executive B&amp;B</title>
<link rel="stylesheet" href="https://fonts.googleapis.com/css2?family=Open+Sans:wght@300;400;600;700&display=swap">
<style>
:root{
  --accent:#ef1d4f;
  --ink:#3a3a3a;
  --muted:#8a8a8a;
  --rule:#cfcfcf;
  --paper:#ffffff;
  --topbar:#2b2b2b;
  --footer:#464646;
  --footer-base:#333333;
  --footer-text:#d9d9d9;
}
*{box-sizing:border-box;margin:0;padding:0}
html,body{width:668px;height:1200px;overflow:hidden;background:var(--paper)}
body{font-family:"Open Sans",Arial,sans-serif;color:var(--ink);position:relative}
.abs{position:absolute}

/* top bar */
.topbar{left:0;top:0;width:668px;height:14px;background:var(--topbar);color:#bbb;font-size:4.5px}
.topbar .contact{left:136px;top:4px;display:flex;gap:12px}
.topbar .social{left:482px;top:4px;display:flex;gap:4px}
.topbar .social span{width:6px;height:6px;background:#e5e5e5;display:block}

/* nav */
.brand{left:136px;top:22px;display:flex;align-items:center;gap:5px}
.brand .dot{width:15px;height:15px;border-radius:50%;background:var(--accent)}
.brand .name{font-size:8.5px;font-weight:600;color:#555;letter-spacing:.2px}
.nav{left:298px;top:27px;display:flex;font-size:4.2px;color:#999;text-transform:uppercase}
.nav a{color:inherit;text-decoration:none;width:32px}
.nav a.active{color:var(--accent)}

/* hero */
.hero{left:4px;top:44px;width:660px;height:156px;background:linear-gradient(100deg,#8e7668 0%,#b7a195 40%,#9c8577 70%,#c8bfb8 100%)}
.hero-title{left:300px;top:64px;width:232px;text-align:center;color:#fff;font-size:14px;font-weight:400;white-space:nowrap}
.hero-title .stars{font-size:9px;letter-spacing:1px}
.hero-sub{left:300px;top:88px;width:232px;text-align:center;color:#fff;font-size:9.5px}
.btn{display:flex;align-items:center;justify-content:center;border-radius:3px;font-size:4.5px;font-weight:600;text-transform:uppercase}
.btn-accent{background:var(--accent);color:#fff}
.see-rooms{left:397px;top:114px;width:40px;height:15px}

/* booking */
.booking{left:136px;top:179px;width:395px;height:43px;background:#fff;border:1px solid #bdbdbd;border-radius:6px}
.field{position:absolute;top:10px;font-size:4px;color:#666}
.field .box{margin-top:3px;height:11px;border:1px solid #ddd;border-radius:2px;font-size:4px;color:#aaa;padding:3px 4px;white-space:nowrap;overflow:hidden}
.book-now{position:absolute;left:330px;top:18px;width:57px;height:13px}

/* section headings */
.heading{width:396px;left:136px;display:flex;align-items:center;gap:14px;font-size:9px;color:var(--muted);font-weight:400}
.heading::before,.heading::after{content:"";flex:1;height:1px;background:var(--rule)}
.heading.half{width:190px}

/* rooms */
.room{top:265px;width:123px;height:99px;border:1px solid #e2e2e2;background:#fff}
.room .photo{height:77px}
.room .label{font-size:4.5px;padding:7px 8px;color:#555}

/* facilities */
.facility{top:419px;width:88px;text-align:center}
.facility .icon{width:29px;height:29px;margin:0 auto;display:block}
.facility h3{font-size:4.6px;font-weight:400;margin-top:8px;color:#444}
.facility p{font-size:4.3px;line-height:5.1px;margin-top:5px;color:#555}
.facility .more{font-size:4.4px;color:var(--accent);margin-top:4px;display:block}

/* promo band */
.band{left:4px;top:520px;width:660px;height:104px;background:linear-gradient(90deg,#b2495f 0%,#c66375 45%,#d7806f 75%,#de8f6a 100%)}
.band-brand{left:270px;top:544px;display:flex;align-items:center;gap:5px}
.band-brand .dot{width:14px;height:14px;border-radius:50%;background:var(--accent)}
.band-brand .name{font-size:7px;font-weight:600;color:#fff}
.band-sub{left:260px;top:565px;width:150px;text-align:center;font-size:6.5px;color:#fff;font-weight:600}
.band-btn{left:301px;top:582px;width:63px;height:16px;background:#fff;color:var(--accent);border-radius:3px;font-size:4.5px;display:flex;align-items:center;justify-content:center}

/* gallery */
.gallery{top:681px;height:139px;width:220px}

/* testimonials */
.avatar{width:36px;height:36px;border-radius:50%;background:#e1e1e1;border:1px solid #cfcfcf}
.quote{width:97px;height:37px;border:1px solid #888;background:#fff;font-size:4.3px;line-height:5px;padding:4px 5px;color:#555}
.quote .who{color:var(--accent);display:block}
.arrow{width:19px;height:19px;border-radius:50%;border:1px solid #bbb;display:flex;align-items:center;justify-content:center}

/* details tabs */
.tabs{left:338px;top:876px;width:188px;height:17px;border-bottom:1px solid #ddd;display:flex;font-size:4.2px}
.tabs span{padding:6px 7px;color:var(--accent)}
.tabs .on{color:#444;border:1px solid #ddd;border-bottom-color:#fff;background:#fff}
.details-text{left:341px;top:898px;width:186px;font-size:4.3px;line-height:5.2px;color:#999}
.details-text p+p{margin-top:3px;width:118px}

/* footer */
.footer{left:4px;top:1026px;width:660px;height:150px;background:var(--footer)}
.footer-base{left:4px;top:1176px;width:660px;height:24px;background:var(--footer-base);color:#bbb;font-size:4px}
.footer-base span{position:absolute;left:130px;top:10px}
.fcol{top:1044px;color:var(--footer-text);font-size:4.2px;line-height:5.2px}
.fcol h4{font-size:4.6px;font-weight:400;text-transform:uppercase;margin-bottom:9px;color:#eee}
.calendar{width:90px;color:#ddd}
.calendar caption{font-size:5px;padding-bottom:4px;text-align:center}
.calendar table{width:100%;border-collapse:collapse;font-size:4px}
.calendar td,.calendar th{height:10px;text-align:left;font-weight:400}
.post{display:flex;gap:5px;padding-bottom:5px;margin-bottom:5px;border-bottom:1px solid #aaa;width:92px}
.post .thumb{width:25px;height:25px;background:#9a7f6c;flex:none}
</style>
</head>
<body>

<header class="abs topbar">
  <div class="abs contact"><span>02 5550 1847</span><span>info@lorvenstays.example</span></div>
  <div class="abs social" aria-label="Social links"><span></span><span></span><span></span></div>
</header>

<div class="abs brand"><span class="dot"></span><span class="name">LORVEN STAYS</span></div>
<nav class="abs nav">
  <a class="active">Home</a><a>Rooms</a><a>B&amp;B</a><a>Gallery</a><a>Location</a><a>Contact</a><a>Blog</a>
</nav>

<section class="abs hero" role="img" aria-label="Photo of the apartment lounge with floral armchairs and a glass dining table"></section>
<h1 class="abs hero-title"><span class="stars">☆☆☆</span> A Four Star Executive B&amp;B <span class="stars">☆☆☆</span></h1>
<p class="abs hero-sub">And we like to keep it that way!</p>
<a class="abs btn btn-accent see-rooms">See rooms</a>

<form class="abs booking">
  <div class="field" style="left:10px;width:89px">E-mail ⓘ<div class="box"></div></div>
  <div class="field" style="left:106px;width:56px">Room Type ⓘ<div class="box">Select a room</div></div>
  <div class="field" style="left:168px;width:59px">Check-in ⓘ<div class="box">Check-in</div></div>
  <div class="field" style="left:234px;width:58px">Check-out ⓘ<div class="box">Check-out</div></div>
  <div class="field" style="left:298px;width:25px">Guests<div class="box" style="color:#666">1 <span style="color:var(--accent)">▴</span></div></div>
  <a class="btn btn-accent book-now">Book now</a>
</form>

<h2 class="abs heading" style="top:236px">Your Rooms</h2>
<article class="abs room" style="left:136px"><div class="photo" role="img" aria-label="Kitchen photo" style="background:linear-gradient(135deg,#8c6a55,#d9d0c6)"></div><div class="label">Kitchen</div></article>
<article class="abs room" style="left:271px"><div class="photo" role="img" aria-label="Bedroom photo with red bedspread" style="background:linear-gradient(180deg,#b38f6c,#b3262b)"></div><div class="label">Bedroom</div></article>
<article class="abs room" style="left:406px"><div class="photo" role="img" aria-label="Bathroom photo" style="background:linear-gradient(90deg,#9aa09b,#d8d6d2)"></div><div class="label">Bathroom</div></article>

<h2 class="abs heading" style="top:391px">Facilities</h2>
<div class="abs facility" style="left:138px">
  <svg class="icon" viewBox="0 0 30 30"><circle cx="15" cy="15" r="14" fill="none" stroke="#ef1d4f" stroke-width="1.2"/><path d="M15 22c-3-4-5-6.5-5-9a5 5 0 0 1 10 0c0 2.5-2 5-5 9z" fill="none" stroke="#ef1d4f" stroke-width="1.2"/><circle cx="15" cy="13" r="1.8" fill="none" stroke="#ef1d4f"/></svg>
  <h3>Great Location</h3>
  <p>Minutes from Deakin offices and both hospitals, with easy parking and quick bus links into Woden and the city centre.</p>
  <span class="more">Read More</span>
</div>
<div class="abs facility" style="left:238px">
  <svg class="icon" viewBox="0 0 30 30"><circle cx="15" cy="15" r="14" fill="none" stroke="#ef1d4f" stroke-width="1.2"/><path d="M10 10l10 10M20 10l-10 10M8 13a9 9 0 0 1 14 0" fill="none" stroke="#ef1d4f" stroke-width="1.2"/></svg>
  <h3>FREE WiFi</h3>
  <p>Fast unlimited wireless across the whole apartment, so you can finish reports, join calls and stream in the evening.</p>
  <span class="more">Read More</span>
</div>
<div class="abs facility" style="left:340px">
  <svg class="icon" viewBox="0 0 30 30"><circle cx="15" cy="15" r="14" fill="none" stroke="#ef1d4f" stroke-width="1.2"/><rect x="8" y="10" width="14" height="10" rx="1" fill="none" stroke="#ef1d4f" stroke-width="1.2"/><path d="M12 7l3 3 3-3M12 22h6" fill="none" stroke="#ef1d4f" stroke-width="1.2"/></svg>
  <h3>FREE CABLE TV</h3>
  <p>A full pay TV package with sport, movies and news channels on a large flat screen in the lounge room.</p>
  <span class="more">Read More</span>
</div>
<div class="abs facility" style="left:440px">
  <svg class="icon" viewBox="0 0 30 30"><circle cx="15" cy="15" r="14" fill="none" stroke="#ef1d4f" stroke-width="1.2"/><circle cx="15" cy="11" r="3" fill="#ef1d4f"/><path d="M11 22l2-8h4l2 8z" fill="#ef1d4f"/></svg>
  <h3>Private facilities</h3>
  <p>Your own entrance, kitchen, laundry and bathroom, kept private for your stay with nothing shared with other guests.</p>
  <span class="more">Read More</span>
</div>

<section class="abs band" role="img" aria-label="Courtyard with outdoor table and autumn foliage under a pink tint"></section>
<div class="abs band-brand"><span class="dot"></span><span class="name">LORVEN STAYS</span></div>
<p class="abs band-sub">AN EXECUTIVE BED &amp; BREAKFAST</p>
<a class="abs band-btn">Check out our blog</a>

<h2 class="abs heading" style="top:652px">Gallery</h2>
<div class="abs gallery" style="left:4px;background:linear-gradient(120deg,#7a6a5c,#c9b79c 55%,#e6dccb)" role="img" aria-label="Living room with television and glass coffee table"></div>
<div class="abs gallery" style="left:224px;background:linear-gradient(90deg,#c8c2b6,#9a6a58 45%,#5e7a3c)" role="img" aria-label="Brick courtyard entrance with garden"></div>
<div class="abs gallery" style="left:444px;background:linear-gradient(90deg,#cfc7ba,#efece6 60%,#b8ab98)" role="img" aria-label="Laundry with washing machine"></div>

<h2 class="abs heading half" style="top:849px;left:136px">What our customers say</h2>
<h2 class="abs heading half" style="top:849px;left:338px">Details</h2>

<div class="abs arrow" style="left:135px;top:907px"><svg width="6" height="8" viewBox="0 0 6 8"><path d="M5 1L2 4l3 3" fill="none" stroke="#888" stroke-width="1"/></svg></div>
<div class="abs arrow" style="left:304px;top:907px"><svg width="6" height="8" viewBox="0 0 6 8"><path d="M1 1l3 3-3 3" fill="none" stroke="#888" stroke-width="1"/></svg></div>
<div class="abs avatar" style="left:160px;top:876px" role="img" aria-label="Guest portrait placeholder"></div>
<blockquote class="abs quote" style="left:202px;top:878px">Quiet, spotless and close to the hospital. Everything I needed for a two week contract was already there.<span class="who">Tom Reyes</span></blockquote>
<div class="abs avatar" style="left:160px;top:920px" role="img" aria-label="Guest portrait placeholder"></div>
<blockquote class="abs quote" style="left:202px;top:919px">Lovely hosts and a comfortable bed. Check in was simple and the kitchen had all the basics ready.<span class="who">Clara Whitfield</span></blockquote>

<div class="abs tabs"><span class="on">Our Rooms</span><span>Facilities</span><span>Location</span></div>
<div class="abs details-text">
  <p>A self contained executive apartment in Deakin with a queen bedroom, full kitchen, laundry and a sunny courtyard. Ideal for contractors and public servants on short or long stays near Woden and the hospitals.</p>
  <p>Linen, towels and breakfast supplies are provided. Weekly cleaning is included and secure parking sits right outside your door.</p>
</div>

<footer class="abs footer"></footer>
<div class="abs fcol" style="left:134px;width:92px">
  <h4>About</h4>
  <p>Lorven Stays offers a quiet executive bed and breakfast in Deakin, built for people working in Canberra who want a home base rather than a hotel room. Book direct for the best rate and flexible dates.</p>
</div>
<div class="abs fcol" style="left:237px">
  <h4>Calendar</h4>
  <div class="calendar">
    <table>
      <caption>November 2015</caption>
      <tr><th>M</th><th>T</th><th>W</th><th>T</th><th>F</th><th>S</th><th>S</th></tr>
      <tr><td></td><td></td><td></td><td></td><td></td><td></td><td>1</td></tr>
      <tr><td>2</td><td>3</td><td>4</td><td>5</td><td>6</td><td>7</td><td>8</td></tr>
      <tr><td>9</td><td>10</td><td>11</td><td>12</td><td>13</td><td>14</td><td>15</td></tr>
      <tr><td>16</td><td>17</td><td>18</td><td>19</td><td>20</td><td>21</td><td>22</td></tr>
      <tr><td>23</td><td>24</td><td>25</td><td>26</td><td>27</td><td>28</td><td>29</td></tr>
      <tr><td>30</td><td></td><td></td><td></td><td></td><td></td><td></td></tr>
      <tr><td colspan="7">&lt;&lt; OCT</td></tr>
    </table>
  </div>
</div>
<div class="abs fcol" style="left:338px">
  <h4>From our blog</h4>
  <div class="post"><div class="thumb" role="img" aria-label="Blog thumbnail"></div><div>Renovation complete<br><br>March 18, 2015</div></div>
  <div class="post"><div class="thumb" role="img" aria-label="Blog thumbnail"></div><div>Another Post<br><br>April 10, 2015</div></div>
  <div class="post" style="border:0"><div class="thumb" role="img" aria-label="Blog thumbnail" style="background:#a6484a"></div><div>Another Post<br><br>May 12, 2015</div></div>
</div>
<div class="abs fcol" style="left:438px">
  <h4>Address</h4>
  <p>LORVEN STAYS</p><br>
  <p>Halden Crescent<br>Deakin</p><br>
  <p>P: 0400 555 101<br>&nbsp;&nbsp;&nbsp;&nbsp;0400 555 202<br>&nbsp;&nbsp;&nbsp;&nbsp;0400 555 303<br>E: info@lorvenstays.example</p><br>
  <p>W: lorvenstays.example</p>
</div>
<div class="abs footer-base"><span>© Lorven Stays all rights reserved</span></div>

</body>
</html>
```